Business card and stationary for a Massage Therapist
Kneading Haven Studio
Business card and stationary for a Massage Therapist - Massage Therapy
Creative Brief
Professional
Gwen Holloway M.S., L.M.T
Orchard Commons 412 Rte. 9B Dennis, MA 02638
studio@fernwickmail.com
www.kneadinghavenstudio.com

```html
<!DOCTYPE html>
<html lang="en">
<head>
<meta charset="utf-8">
<title>Kneading Haven Studio – Stationery Set</title>
<link href="https://fonts.googleapis.com/css2?family=Great+Vibes&family=Lato:wght@400;700&display=swap" rel="stylesheet">
<style>
:root{
  --backdrop:#8e9398;
  --backdrop-light:#a7abb0;
  --paper:#ffffff;
  --brand-blue:#b7c7d2;
  --brand-blue-deep:#8fa6b6;
  --ink:#5f7384;
  --ink-soft:#9aa9b5;
  --label:#e6e9ec;
  --illustration-a:#dfe6ec;
  --illustration-b:#c4d1db;
}
*{box-sizing:border-box;margin:0;padding:0}
html,body{width:1200px;height:482px;overflow:hidden}
body{background:radial-gradient(ellipse at 50% 45%,var(--backdrop-light),var(--backdrop) 75%);font-family:'Lato',sans-serif;color:var(--ink);position:relative}
.piece{position:absolute;box-shadow:0 2px 5px rgba(0,0,0,.25)}
.item-label{position:absolute;font-size:7px;color:var(--label);letter-spacing:.3px;text-align:center}
.brand{display:flex;flex-direction:column;align-items:center;gap:4px}
.brand-dot{width:14px;height:14px;border-radius:50%;background:var(--ink-soft)}
.brand-name{font-family:'Great Vibes',cursive;color:var(--ink);line-height:1;text-align:center;white-space:nowrap}
.illustration{position:absolute;background:radial-gradient(ellipse at 60% 55%,var(--illustration-b),var(--illustration-a) 60%,rgba(255,255,255,0) 72%)}
/* folder */
.folder{left:46px;top:60px;width:424px;height:384px;display:flex}
.folder-flap{position:absolute;top:130px;width:18px;height:120px;background:var(--paper);box-shadow:0 2px 4px rgba(0,0,0,.2)}
.folder-cover{width:50%;height:100%;background:var(--brand-blue);position:relative;overflow:hidden}
.folder-inside{width:50%;height:100%;background:var(--paper);position:relative;overflow:hidden}
.folder .brand{position:absolute;top:112px;left:14px;right:14px}
.folder .brand-name{font-size:30px;white-space:normal;line-height:1.05}
.folder-pocket{position:absolute;left:0;right:0;bottom:0;height:84px;border-top:1px solid rgba(0,0,0,.08)}
.folder-cover .folder-pocket{background:var(--brand-blue-deep);opacity:.35}
.pocket-tab{position:absolute;bottom:22px;left:50%;width:36px;height:18px;margin-left:-18px;border-radius:18px 18px 0 0;background:var(--brand-blue-deep)}
/* cd */
.cd{left:506px;top:20px;width:106px;height:106px;border-radius:50%;background:var(--paper);display:flex;align-items:center;justify-content:center;overflow:hidden}
.cd-hole{position:absolute;width:16px;height:16px;border-radius:50%;background:var(--backdrop);left:45px;top:45px}
.cd .brand{margin-top:-40px;position:relative}
.cd .brand-name{font-size:10px}
.cd .brand-dot{width:8px;height:8px}
/* cards */
.card{background:var(--paper);padding:6px;overflow:hidden}
.card .brand-name{font-size:11px}
.card .brand-dot{width:9px;height:9px}
.card-square{left:640px;top:34px;width:112px;height:110px}
.card-square .brand{margin-top:10px;position:relative}
.card-small{width:96px;height:52px;font-size:4.6px;line-height:1.5}
.card-small.blue{background:var(--brand-blue)}
.card-small strong{display:block;font-size:5.6px}
.card-small .brand{flex-direction:row;gap:3px}
.card-small .brand-name{font-size:8px}
.card-small .brand-dot{width:6px;height:6px}
/* letterheads */
.letterhead{background:var(--paper);width:192px;height:276px;top:168px;padding:14px;overflow:hidden}
.letterhead .brand{margin-bottom:14px}
.letterhead .brand-name{font-size:14px}
.invoice-table{width:86px;border-collapse:collapse;font-size:5px;color:var(--ink)}
.invoice-table td{border:1px solid var(--ink-soft);padding:1px 3px;height:9px}
.invoice-table td:first-child{background:var(--brand-blue);width:34px}
.letter-foot{position:absolute;bottom:8px;left:14px;right:14px;font-size:4.5px;color:var(--ink-soft);white-space:nowrap;overflow:hidden}
/* envelopes */
.envelope{background:var(--paper);overflow:hidden}
.envelope svg{position:absolute;left:0;top:0}
.envelope .brand{position:absolute;left:0;right:0}
.envelope .brand-name{font-size:11px}
.address{position:absolute;font-size:5px;line-height:1.5;color:var(--ink)}
</style>
</head>
<body>

<!-- Presentation folder -->
<div class="item-label" style="left:46px;top:49px;width:424px">Presentation Folder</div>
<div class="folder-flap" style="left:28px;top:190px"></div>
<div class="piece folder">
  <div class="folder-cover">
    <div class="brand"><span class="brand-dot"></span><span class="brand-name">Kneading Haven<br>Studio</span></div>
    <div class="folder-pocket"></div>
    <div class="pocket-tab"></div>
  </div>
  <div class="folder-inside">
    <div class="illustration" role="img" aria-label="Soft illustration of open hands cradling a shell" style="left:60px;top:90px;width:150px;height:230px"></div>
    <div class="folder-pocket"></div>
    <div class="pocket-tab"></div>
  </div>
</div>

<!-- CD -->
<div class="item-label" style="left:506px;top:10px;width:106px">CD</div>
<div class="piece cd">
  <div class="illustration" role="img" aria-label="Hands and shell motif" style="left:46px;top:38px;width:56px;height:64px"></div>
  <div class="cd-hole"></div>
  <div class="brand"><span class="brand-dot"></span><span class="brand-name">Kneading Haven Studio</span></div>
</div>

<!-- Business cards -->
<div class="item-label" style="left:640px;top:24px;width:320px">Business Card</div>
<div class="piece card card-square">
  <div class="illustration" role="img" aria-label="Hands holding a shell" style="left:38px;top:28px;width:74px;height:82px"></div>
  <div class="brand"><span class="brand-dot"></span><span class="brand-name">Kneading Haven Studio</span></div>
</div>
<div class="piece card card-small" style="left:760px;top:34px">
  <div class="brand"><span class="brand-dot"></span><span class="brand-name">Kneading Haven Studio</span></div>
  <strong>Gwen Holloway M.S., L.M.T</strong>
  Orchard Commons 412 Rte. 9B<br>Dennis, MA 02638
</div>
<div class="piece card card-small blue" style="left:760px;top:92px">
  <strong>Gwen Holloway M.S., L.M.T</strong>
  studio@fernwickmail.com<br>www.kneadinghavenstudio.com
</div>
<div class="piece card card-small" style="left:864px;top:34px">
  <strong>Gwen Holloway M.S., L.M.T</strong>
  Orchard Commons 412 Rte. 9B<br>Dennis, MA 02638<br>studio@fernwickmail.com
</div>
<div class="piece card card-small blue" style="left:864px;top:92px">
  <div class="brand"><span class="brand-dot"></span><span class="brand-name">Kneading Haven Studio</span></div>
  www.kneadinghavenstudio.com
</div>

<!-- Small envelope -->
<div class="item-label" style="left:975px;top:24px;width:150px">Envelope</div>
<div class="piece envelope" style="left:975px;top:34px;width:150px;height:70px">
  <div class="address" style="left:8px;top:8px">Kneading Haven Studio<br>412 Rte. 9B, Dennis, MA 02638</div>
  <div class="address" style="left:70px;top:38px">Gwen Holloway<br>Orchard Commons</div>
</div>

<!-- Letterheads -->
<div class="item-label" style="left:499px;top:158px;width:192px">Invoice</div>
<div class="piece letterhead" style="left:499px">
  <div class="illustration" role="img" aria-label="Faint hands and shell watermark" style="left:82px;top:126px;width:110px;height:150px"></div>
  <table class="invoice-table">
    <tr><td>Date</td><td></td></tr>
    <tr><td>Client</td><td></td></tr>
    <tr><td>Service</td><td></td></tr>
    <tr><td>Hours</td><td></td></tr>
    <tr><td>Total</td><td></td></tr>
  </table>
  <div class="letter-foot">Orchard Commons · 412 Rte. 9B · Dennis, MA 02638 · studio@fernwickmail.com</div>
</div>
<div class="item-label" style="left:703px;top:158px;width:192px">Letterhead</div>
<div class="piece letterhead" style="left:703px">
  <div class="illustration" role="img" aria-label="Faint hands and shell watermark" style="left:82px;top:126px;width:110px;height:150px"></div>
  <div class="brand"><span class="brand-dot"></span><span class="brand-name">Kneading Haven Studio</span></div>
  <div class="letter-foot">Orchard Commons · 412 Rte. 9B · Dennis, MA 02638 · www.kneadinghavenstudio.com</div>
</div>

<!-- Envelopes -->
<div class="piece envelope" style="left:912px;top:222px;width:264px;height:102px">
  <svg width="264" height="102" viewBox="0 0 264 102" aria-hidden="true">
    <path d="M0 0 L132 52 L264 0 Z" fill="var(--brand-blue)"/>
    <path d="M0 102 L132 44 L264 102" fill="none" stroke="#e3e8ec" stroke-width="1"/>
  </svg>
  <div class="brand" style="top:40px"><span class="brand-dot" style="width:10px;height:10px"></span></div>
</div>
<div class="piece envelope" style="left:912px;top:336px;width:264px;height:108px;background:var(--brand-blue)">
  <svg width="264" height="108" viewBox="0 0 264 108" aria-hidden="true">
    <path d="M0 0 L132 46 L264 0 Z" fill="var(--brand-blue-deep)"/>
  </svg>
</div>
<div class="piece envelope" style="left:960px;top:370px;width:216px;height:74px">
  <svg width="216" height="74" viewBox="0 0 216 74" aria-hidden="true">
    <path d="M0 0 L108 30 L216 0 Z" fill="var(--brand-blue)"/>
  </svg>
  <div class="brand" style="top:22px"><span class="brand-dot" style="width:10px;height:10px"></span></div>
</div>

</body>
</html>
```